Business card design needed

we do security the old cards we have are very out of date
i would love something with a fox and fire that pops
as you could tell on the description we do cctv and alarms so if you could add that some how it would be perfect
thank you very much
Industry/Entity Type
Security
Contact Information for Business Card
Wrenlock industries Pty Ltd
Intruder alarms / access contol. cctv sales . service , installation repairs & 24 hour monitoring
Colin Marsh - technician
ph: 07 38516204
fax: 07 38516294
mob: 0418732945
email: colinm@bluvanta.com.au
ABN: 46 219 807 352

```html
<!DOCTYPE html>
<html lang="en">
<head>
<meta charset="utf-8">
<title>Wrenlock industries – Business Card</title>
<link rel="stylesheet" href="https://fonts.googleapis.com/css2?family=PT+Serif:wght@400&display=swap">
<style>
  :root {
    --card-bg: #ffffff;
    --brand-grey: #a0a0a0;
    --ink-dark: #111111;
    --ink-mid: #333333;
    --ink-soft: #555555;
  }
  html, body {
    margin: 0;
    padding: 0;
    width: 1200px;
    height: 693px;
    overflow: hidden;
    background: var(--card-bg);
  }
  .card {
    position: relative;
    width: 1200px;
    height: 693px;
    background: var(--card-bg);
    font-family: "PT Serif", "Palatino Linotype", Georgia, serif;
  }
  .brand-mark {
    position: absolute;
    left: 59px;
    top: 120px;
    width: 236px;
    height: 236px;
  }
  .brand-mark-name {
    position: absolute;
    left: 59px;
    top: 120px;
    width: 236px;
    height: 236px;
    display: flex;
    align-items: center;
    justify-content: center;
    font-size: 34px;
    color: var(--ink-dark);
    line-height: 1;
  }
  .line {
    position: absolute;
    left: 420px;
    margin: 0;
    white-space: nowrap;
    line-height: 1;
  }
  .company-name { top: 140px; font-size: 50px; color: var(--ink-dark); }
  .services     { font-size: 25px; color: var(--ink-mid); }
  .services-1   { top: 197px; }
  .services-2   { top: 237px; }
  .person-name  { top: 334px; font-size: 43px; color: var(--ink-soft); }
  .contact      { font-size: 34px; color: var(--ink-soft); }
  .contact-phone  { top: 403px; }
  .contact-fax    { top: 448px; }
  .contact-mobile { top: 493px; }
  .contact-email  { top: 563px; }
  .contact-abn    { top: 609px; }
</style>
</head>
<body>
  <main class="card">
    <svg class="brand-mark" viewBox="0 0 236 236" aria-hidden="true">
      <circle cx="118" cy="118" r="118" fill="var(--brand-grey)"/>
    </svg>
    <div class="brand-mark-name">Wrenlock</div>

    <h1 class="line company-name" style="font-weight:400">Wrenlock industries</h1>
    <p class="line services services-1">Pty Ltd Intruder alarms / access contol. cctv sales.</p>
    <p class="line services services-2">Service, installation repairs &amp; 24 hour monitoring</p>

    <h2 class="line person-name" style="font-weight:400">Colin Marsh</h2>
    <p class="line contact contact-phone">Technician phone: 07 38516204</p>
    <p class="line contact contact-fax">fax: 07 38516294</p>
    <p class="line contact contact-mobile">mobile: 0418732945</p>
    <p class="line contact contact-email">Email: colinm@bluvanta.com.au</p>
    <p class="line contact contact-abn">ABN: 46 219 807 352</p>
  </main>
</body>
</html>
```